Casa and Valor Website Re-design

Already Wordpress base. Needs to be updated and better presentation. Current site: www.valorcasa.example redirected from www.casaandvalors.example
Site purpose is to offer information and get leads from potential heroes looking to buy, rent or sell a home
Here is a link to the video to be used as well: https://www.videohost.example/watch?v=Lm8RtPz3VwK

I own the video and logo
The video spells out the program. We will need a page for REALTORS to sign up, a page for our Vendors and their benefits
Steadfast Lending, Marpen Odari offers a reduced rate plus they will pay the upfront cost of the $600 VA appraisal
Hero Buyers get 25% rebate after escrow
Hero Sellers get 25% off a normal 6% Listing
Copperfield Inspections will give a 10% off discount for heroes
Also need a page for the Medic Gives program

Direct competitor: www.nestsforvalor.example

Target Market(s)

veterans, teachers, government employees, nurses, 1st responders

Industry/Entity Type

Realtor

Coding

Coded - Design and coding required

Number of Pages Required

5+ page

Colors
ec1f27
ffffff
3176b5

Requirements
Must have
• clean and correct throughout, ability to collect leads with FB login, or names and phone and email information. Colors are Navy Blue, Burgandy Red, and White
Nice to have
• photos

```html
<!DOCTYPE html>
<html lang="en">
<head>
<meta charset="utf-8">
<title>Casa and Valor</title>
<link href="https://fonts.googleapis.com/css2?family=Roboto:wght@400;500;700&family=Open+Sans:wght@400;600&display=swap" rel="stylesheet">
<style>
:root{
  --blue:#3176b5;
  --blue-dark:#2a66a0;
  --red:#ec1f27;
  --navy:#1b2f5e;
  --ink:#222;
  --text:#333;
  --light:#eef1f5;
  --white:#fff;
}
*{box-sizing:border-box;margin:0;padding:0}
html,body{width:1200px;height:2493px;overflow:hidden}
body{position:relative;background:var(--white);font-family:'Open Sans',sans-serif;color:var(--text)}
.abs{position:absolute}

/* header */
.site-header{position:absolute;left:0;top:0;width:1200px;height:111px;background:var(--white)}
.brand{position:absolute;left:86px;top:30px;font-family:'Roboto',sans-serif;font-weight:700;font-size:30px;color:var(--navy);line-height:1.2}
.phone{position:absolute;right:85px;top:20px;display:flex;align-items:center;gap:12px;color:var(--red);font-family:'Roboto',sans-serif;font-size:17px}
.phone-dot{width:32px;height:32px;border-radius:50%;background:var(--blue);display:flex;align-items:center;justify-content:center}
.main-nav{position:absolute;right:85px;top:70px;display:flex;gap:50px;font-family:'Roboto',sans-serif;font-size:14px;font-weight:500;color:var(--ink);align-items:center}
.main-nav .active{color:var(--blue)}

/* hero */
.hero{position:absolute;left:0;top:111px;width:1200px;height:437px;background:linear-gradient(180deg,#6d7a8c 0%,#8d97a3 40%,#5f6b56 75%,#3f5a34 100%)}
.hero-title{position:absolute;left:0;top:148px;width:1200px;text-align:center;font-family:'Roboto',sans-serif;font-weight:700;font-size:92px;color:var(--navy);line-height:1.1}

/* what we do */
.section-title{position:absolute;width:1200px;left:0;text-align:center;font-family:'Roboto',sans-serif;font-weight:400;font-size:40px;color:var(--blue)}
.people{position:absolute;left:133px;top:681px;width:906px;height:308px;background:linear-gradient(90deg,#c9cfc0,#e7e0dc 40%,#dfe6ee 70%,#e6edf5)}
.services-bar{position:absolute;left:86px;top:986px;width:1028px;height:8px;background:var(--red)}
.services{position:absolute;left:86px;top:994px;width:1028px;height:261px;background:var(--blue);box-shadow:0 28px 22px -18px rgba(0,0,0,.45)}
.services-pointer{position:absolute;left:600px;top:994px;width:0;height:0;border-left:14px solid transparent;border-right:14px solid transparent;border-top:14px solid var(--red);transform:translateX(-14px)}
.service{position:absolute;top:45px;width:180px;text-align:center;transform:translateX(-90px)}
.service-icon{width:132px;height:132px;margin:0 auto;border-radius:50%;border:4px solid var(--white);display:flex;align-items:center;justify-content:center;background:var(--blue)}
.service-icon .disc{width:112px;height:112px;border-radius:50%;background:var(--white);display:flex;align-items:center;justify-content:center}
.service.on .service-icon .disc{background:var(--red)}
.service-label{margin-top:24px;font-family:'Roboto',sans-serif;font-weight:500;font-size:17px;color:var(--white)}

/* how it works */
.how-title{position:absolute;left:83px;top:1332px;font-family:'Roboto',sans-serif;font-size:43px;color:var(--blue)}
.how-rule{position:absolute;left:86px;top:1398px;width:68px;height:2px;background:var(--blue)}
.how-copy{position:absolute;left:86px;top:1422px;width:410px;font-size:12.8px;line-height:22px;color:var(--text)}
.how-copy p+p{margin-top:22px}
.btn{position:absolute;left:86px;top:1640px;width:113px;height:44px;background:var(--blue);color:var(--white);font-family:'Roboto',sans-serif;font-weight:700;font-size:13px;display:flex;align-items:center;justify-content:center;border-radius:2px}
.video{position:absolute;left:550px;top:1341px;width:562px;height:341px;background:#000}
.video-art{position:absolute;left:0;top:22px;width:562px;height:292px;background:linear-gradient(120deg,#2b4d9a,#1e3a84 60%,#1a3274)}
.video-controls{position:absolute;left:0;bottom:0;width:562px;height:27px;background:#1b1b1b;display:flex;align-items:center;gap:14px;padding:0 12px}

/* testimonials */
.testimonials{position:absolute;left:0;top:1762px;width:1200px;height:394px;background:linear-gradient(180deg,#3a7cbd,#2f70b0)}
.testimonials .section-title{color:var(--white);top:54px}
.t-rule{position:absolute;left:527px;top:111px;width:146px;height:1px;background:rgba(255,255,255,.6)}
.avatar{position:absolute;left:122px;top:150px;width:132px;height:132px;border-radius:50%;border:4px solid #c8d4e4;background:linear-gradient(135deg,#c7a48e,#6d6a55)}
.t-divider{position:absolute;left:305px;top:153px;width:2px;height:126px;background:rgba(255,255,255,.7)}
.quote{position:absolute;left:366px;top:160px;width:730px;font-size:13.4px;line-height:24px;color:var(--white)}
.t-name{position:absolute;left:366px;top:260px;font-family:'Roboto',sans-serif;font-size:20px;color:var(--white)}
.t-arrow{position:absolute;top:304px;width:24px;height:24px;display:flex;align-items:center;justify-content:center}
.t-prev{left:364px;background:var(--red)}
.t-next{left:394px;background:#222}

/* footer */
.site-footer{position:absolute;left:0;top:2156px;width:1200px;height:265px;background:var(--light)}
.footer-brand{position:absolute;left:86px;top:85px;font-family:'Roboto',sans-serif;font-weight:700;font-size:48px;color:var(--navy)}
.footer-head{position:absolute;top:48px;font-family:'Roboto',sans-serif;font-weight:500;font-size:17px;color:var(--blue)}
.quick-links{position:absolute;left:520px;top:88px;list-style:none;font-size:12px;line-height:26px;color:#444}
.quick-links li::before{content:">";margin-right:10px}
.signup{position:absolute;left:795px;top:89px;width:319px;height:42px;display:flex}
.signup-input{flex:1;background:var(--white);border:1px solid #d5d9de;font-size:12px;color:#777;display:flex;align-items:center;padding-left:12px}
.signup-btn{width:102px;background:var(--red);color:var(--white);font-family:'Roboto',sans-serif;font-weight:500;font-size:16px;display:flex;align-items:center;justify-content:center}
.social{position:absolute;left:797px;top:165px;display:flex;gap:8px}
.social span{width:22px;height:22px;border-radius:50%}
.copyright{position:absolute;left:0;top:2421px;width:1200px;height:72px;background:var(--blue);color:var(--white);font-size:14px;display:flex;align-items:center;justify-content:center}
</style>
</head>
<body>

<header class="site-header">
  <div class="brand">Casa and Valor</div>
  <div class="phone">
    <span class="phone-dot"><svg width="16" height="16" viewBox="0 0 24 24"><path fill="#fff" d="M6.6 10.8a15 15 0 006.6 6.6l2.2-2.2a1 1 0 011-.25 11.4 11.4 0 003.6.57 1 1 0 011 1V20a1 1 0 01-1 1A17 17 0 013 4a1 1 0 011-1h3.5a1 1 0 011 1c0 1.25.2 2.45.57 3.57a1 1 0 01-.25 1z"/></svg></span>
    (555)010-NEST
  </div>
  <nav class="main-nav">
    <span class="active">Home</span><span>How It Works</span><span>Contact Us</span><span>Hero Advantages</span>
    <svg width="14" height="14" viewBox="0 0 24 24"><circle cx="10" cy="10" r="6.5" fill="none" stroke="#ec1f27" stroke-width="3"/><path d="M15 15l6 6" stroke="#ec1f27" stroke-width="3"/></svg>
  </nav>
</header>

<section class="hero" role="img" aria-label="Photo of a large suburban home with a landscaped front yard">
  <div class="hero-title">Casa and Valor</div>
</section>

<h2 class="section-title" style="top:606px">WHAT WE DO</h2>
<div class="people" role="img" aria-label="Photo of five heroes standing together: a soldier, a firefighter, a police officer, a doctor and a teacher"></div>
<div class="services-bar"></div>
<section class="services">
  <div class="service" style="left:153px">
    <div class="service-icon"><div class="disc"><svg width="56" height="56" viewBox="0 0 56 56"><path d="M8 34a20 20 0 0140 0v6H8z" fill="#1b2f5e"/><rect x="4" y="40" width="48" height="6" fill="#1b2f5e"/><path d="M22 24l6 4 6-4M22 30l6 4 6-4" stroke="#fff" stroke-width="2.5" fill="none"/></svg></div></div>
    <div class="service-label">MILITARY</div>
  </div>
  <div class="service" style="left:333px">
    <div class="service-icon"><div class="disc"><svg width="56" height="56" viewBox="0 0 56 56"><rect x="20" y="8" width="16" height="8" rx="3" fill="#1b2f5e"/><rect x="16" y="16" width="24" height="4" fill="#1b2f5e"/><rect x="18" y="20" width="20" height="26" fill="#1b2f5e"/><rect x="10" y="26" width="36" height="8" rx="2" fill="#1b2f5e"/><rect x="14" y="46" width="28" height="5" fill="#1b2f5e"/></svg></div></div>
    <div class="service-label">FIREFIGHTERS</div>
  </div>
  <div class="service on" style="left:514px">
    <div class="service-icon"><div class="disc"><svg width="56" height="56" viewBox="0 0 56 56"><g transform="rotate(-40 26 22)"><rect x="14" y="12" width="22" height="10" fill="#fff"/><rect x="23" y="22" width="4" height="20" fill="#fff"/></g><rect x="10" y="42" width="28" height="6" fill="#fff"/><rect x="6" y="48" width="36" height="4" fill="#fff"/></svg></div></div>
    <div class="service-label">LAW ENFORCEMENT</div>
  </div>
  <div class="service" style="left:695px">
    <div class="service-icon"><div class="disc"><svg width="56" height="56" viewBox="0 0 56 56"><path d="M6 40a22 22 0 0144 0z" fill="#1b2f5e"/><rect x="6" y="40" width="44" height="6" fill="#1b2f5e"/><path d="M24 22h8v6h6v8h-6v6h-8v-6h-6v-8h6z" fill="#fff"/></svg></div></div>
    <div class="service-label">HEALTHCARE</div>
  </div>
  <div class="service" style="left:875px">
    <div class="service-icon"><div class="disc"><svg width="56" height="56" viewBox="0 0 56 56"><path d="M28 12L4 22l24 10 24-10z" fill="#1b2f5e"/><path d="M14 28v10c0 4 28 4 28 0V28l-14 6z" fill="#1b2f5e"/><path d="M48 23v14" stroke="#1b2f5e" stroke-width="2.5"/></svg></div></div>
    <div class="service-label">TEACHERS</div>
  </div>
</section>
<div class="services-pointer"></div>

<h2 class="how-title">HOW IT WORKS</h2>
<div class="how-rule"></div>
<div class="how-copy">
  <p>Lenders don’t want borrowers receiving money upfront and so the Casa and Valor program gives a cash rebate at the close of escrow. Since the Casa and Valor program gives cash back at the close of escrow, it does not affect any other loan programs and/or discounts.</p>
  <p>On the purchase of a home, participating buying agents donate 25% of their commission to the Casa and Valor non-profit program. C&amp;V then gives the hero a cash rebate upon close of escrow from.</p>
</div>
<div class="btn">Read More</div>

<div class="video">
  <div class="video-art" role="img" aria-label="Video still: cartoon agent waving beside a speech bubble with the headline Local Hero, we have great news for you"></div>
  <div class="video-controls">
    <svg width="12" height="12" viewBox="0 0 12 12"><path d="M2 1l9 5-9 5z" fill="#ccc"/></svg>
    <svg width="14" height="12" viewBox="0 0 14 12"><path d="M1 4h3l4-3v10L4 8H1z" fill="#ccc"/></svg>
  </div>
</div>

<section class="testimonials">
  <h2 class="section-title">WHAT THEY SAY ABOUT US</h2>
  <div class="t-rule"></div>
  <div class="avatar" role="img" aria-label="Photo of a military family"></div>
  <div class="t-divider"></div>
  <p class="quote">“Lorem Ipsum is simply dummy text of the printing and typesetting industry. Lorem Ipsum has been the industry’s standard dummy text ever since the 1500s, when an unknown printer took a galley of type and scrambled it to make a type specimen book.”</p>
  <div class="t-name">- Dara L Whitcombe</div>
  <div class="t-arrow t-prev"><svg width="10" height="10" viewBox="0 0 10 10"><path d="M7 1L3 5l4 4" stroke="#fff" stroke-width="1.6" fill="none"/></svg></div>
  <div class="t-arrow t-next"><svg width="10" height="10" viewBox="0 0 10 10"><path d="M3 1l4 4-4 4" stroke="#fff" stroke-width="1.6" fill="none"/></svg></div>
</section>

<footer class="site-footer">
  <div class="footer-brand">Casa and Valor</div>
  <div class="footer-head" style="left:520px">QUICK LINKS</div>
  <ul class="quick-links">
    <li>HOME</li><li>HOW IT WORKS</li><li>CONTACT US</li><li>HERO ADVANTAGES</li>
  </ul>
  <div class="footer-head" style="left:795px">STAY IN TOUCH</div>
  <div class="signup"><div class="signup-input">Enter your email</div><div class="signup-btn">SIGN UP</div></div>
  <div class="social"><span style="background:#3b5998"></span><span style="background:#2aa3ef"></span><span style="background:#c13584"></span></div>
</footer>
<div class="copyright">Copyright (c) 2017 Casa and Valor. All rights reserved.</div>

</body>
</html>
```